World first health care product in tablet form to help save relationships and marriages

The product known as Zentharo is in tablet form 470mg and has 30 to a packet the packet size is approx 11cm in length x 4cm We want to use the color of the image attached for the package and cornflower blue for our name Zentharo. We also need to mention close to our name....... maintaining relationships with increased libido and desire ...... Our tablets are in a tamper-proof blister pack inserted into the package. We do not have a logo as yet, we are thinking of zen in small white letters and then THARO in large letters in cornflower blue or something a bit darker. (The O could also contain a smiley face) We are not that fussed with a logo as yet, maybe down the track if our product works and sells. As of today business in Australia has ground to a halt with this coronavirus and its as bad as you could imagine. Please help us make this new product work with a fabulous packet design.
Target Market(s)
females and males
Industry/Entity Type
Pharmaceutical
Requirements
Must have
- the colors of the images attached and cornflower blue

```html
<!DOCTYPE html>
<html lang="en">
<head>
<meta charset="utf-8">
<title>Zentharo – Tablet Pack Label</title>
<link href="https://fonts.googleapis.com/css2?family=Oswald:wght@300;400;500&display=swap" rel="stylesheet">
<style>
  :root {
    --page-bg: #ececec;
    --label-bg: #7fd0e2;
    --ink-white: #ffffff;
    --ink-brand: #5a6fb2;
    --ink-table: #3b3b3b;
    --table-bg: #ffffff;
    --trim-line: #e0303a;
    --wave-1: #4cc4ec;
    --wave-2: #2f62b4;
    --wave-3: #4a4fa6;
    --wave-4: #b9cde8;
  }
  * { margin: 0; padding: 0; box-sizing: border-box; }
  html, body { width: 777px; height: 1200px; overflow: hidden; }
  body {
    background: var(--page-bg);
    font-family: "Oswald", "Arial Narrow", sans-serif;
    font-weight: 300;
    color: var(--ink-white);
    position: relative;
  }
  .label {
    position: absolute;
    left: 20px; top: 320px;
    width: 737px; height: 560px;
    background: var(--label-bg);
    overflow: hidden;
  }
  .wave-band {
    position: absolute;
    left: 0; top: 439px;
    width: 100%; height: 121px;
    background: linear-gradient(100deg, var(--wave-4) 0%, var(--wave-1) 14%, var(--wave-2) 30%, var(--wave-3) 46%, var(--wave-1) 62%, var(--wave-4) 68%, var(--wave-2) 80%, var(--wave-3) 100%);
  }
  .trim-line {
    position: absolute;
    left: 27px; top: 29px;
    width: 684px; height: 502px;
    border: 1px solid var(--trim-line);
    pointer-events: none;
  }
  .abs { position: absolute; white-space: nowrap; line-height: 1; }
  .lead { font-weight: 500; }

  .category { left: 158px; top: 59px; font-size: 10.5px; font-weight: 500; }

  .brand-name {
    left: 107px; top: 270px;
    font-size: 27px; font-weight: 400; letter-spacing: 6.5px;
    color: var(--ink-brand);
  }
  .brand-tm { left: 286px; top: 265px; font-size: 7px; font-weight: 400; color: var(--ink-brand); }

  .tagline { left: 107px; top: 303px; font-size: 11.5px; line-height: 13.6px; }

  .count { left: 107px; top: 362px; font-size: 17px; font-weight: 400; }
  .tablet-kind { left: 107px; top: 382px; font-size: 9.5px; font-weight: 400; display: flex; align-items: center; gap: 4px; }
  .tablet-kind svg { width: 8px; height: 8px; }
  .dose { left: 107px; top: 396px; font-size: 11px; font-weight: 400; }
  .expiry { left: 241px; top: 397px; font-size: 10px; font-weight: 400; }

  .formulation-title { left: 440px; top: 66px; font-size: 11.5px; }

  .formula-table {
    position: absolute;
    left: 440px; top: 85px;
    width: 195px; height: 118px;
    background: var(--table-bg);
    border-radius: 3px;
    color: var(--ink-table);
    font-size: 11.5px;
    padding: 6px 12px 6px 9px;
    border-collapse: separate;
    border-spacing: 0;
  }
  .formula-table td { height: 20.8px; line-height: 1; }
  .formula-table .amount { text-align: right; }

  .directions { left: 440px; top: 215px; font-size: 11.5px; }

  .warnings { left: 440px; top: 235px; font-size: 10.5px; line-height: 13.6px; }
  .warnings .lead { font-size: 11.5px; }
  .warnings .inline-brand { font-weight: 400; letter-spacing: 1px; }

  .company { left: 442px; top: 344px; font-size: 10.5px; line-height: 13.6px; font-style: normal; }
</style>
</head>
<body>
  <main class="label">
    <div class="wave-band" role="img" aria-label="Decorative pattern of overlapping blue and violet circles"></div>
    <div class="trim-line"></div>

    <p class="abs category">Dietary Supplement</p>

    <p class="abs brand-name">ZENTHARO</p>
    <span class="abs brand-tm">™</span>

    <p class="abs tagline">Maintaining Relationships<br>With Increased Libido and Desire</p>

    <p class="abs count">30</p>
    <p class="abs tablet-kind">COATED TABLETS
      <svg viewBox="0 0 8 8" aria-hidden="true"><circle cx="4" cy="4" r="4" fill="#fff"/><rect x="1" y="3.5" width="6" height="1" fill="#7fd0e2"/></svg>
    </p>
    <p class="abs dose">470 mg</p>
    <p class="abs expiry">EXP 11/21</p>

    <p class="abs formulation-title"><strong class="lead">FORMULATION:</strong> EACH COATED TABLET CONTAINS</p>
    <table class="formula-table">
      <tr><td>CYANOCOBALAMIN</td><td class="amount">750 mcg</td></tr>
      <tr><td>CHOLECALCIFEROL</td><td class="amount">75 mcg</td></tr>
      <tr><td>ARGININE (L-ARGININE)</td><td class="amount">300 mg</td></tr>
      <tr><td>UBIQUINOL (COENZYME)</td><td class="amount">150 mg</td></tr>
      <tr><td>ALPHA-TOCOPHEROL</td><td class="amount">17 mg</td></tr>
    </table>

    <p class="abs directions"><strong class="lead">DIRECTIONS:</strong> TAKE ONE TABLET DAILY WITH FOOD</p>

    <p class="abs warnings"><strong class="lead">WARNINGS AND CAUTIONS:</strong> Do not use if the<br>
      blister foil is broken on first opening.<br>
      Store below 25° C<br>
      It does not contain sugar, caffeine, gluten or artificial<br>
      stimulants.<br>
      <span class="inline-brand">ZENTHARO</span> is best taken with food. Do not<br>
      take while on Warfarin therapy.</p>

    <address class="abs company">
      Zentharo Pty Ltd ACN 482 317 905<br>
      Ground Level 212 Harlow road<br>
      Harlow Vic 3199 Melbourne Australia<br>
      www.zentharo.com.au<br>
      Proudly Australian owned
    </address>
  </main>
</body>
</html>
```